App Store Screenshot Design for Vaccination Record App (iOS)

Project Description
We are looking for a professional graphic designer to redesign our App Store screenshots for our iOS app Medlo, a personal vaccination record app.
The goal is to significantly improve App Store conversion by creating screenshots that look:
• Clean
• Trustworthy
• Modern
• Medical but friendly
• Suitable for parents and older adults
Our current screenshots feel too “developer-like.” We want to match or exceed the visual quality of top competitors in this category.
⸻
About the App
Medlo helps people:
• Store all their vaccinations in one place
• Upload and scan vaccination proofs. Medlo automatically recognizes vaccines from photos, making imports fast and effortless.
• Receive reminders for boosters and expiring vaccinations
• Manage profiles for family members
• Export records (PDF) for school, work, or travel
Target users:
• Parents (tracking children’s vaccinations)
• Adults 45+
• Travelers
• Caregivers
This is not a children’s app — it’s a serious health utility that must feel reliable and credible.
⸻
Target Audience
Primary:
• Parents
• Older adults (45+)
Secondary:
• Travelers
• Caregivers
Design should feel:
• Calm
• Reassuring
• Clear
• Easy to understand at a glance
⸻
What We Need
1. App Store Screenshot Designs
• iPhone and iPad format (Apple App Store guidelines)
• Approx. 5–7 screenshots
• Focus on benefits, not features
• Short, strong headlines
• Clean UI framing
Important:
These screenshots are marketing visuals for the App Store.
They do NOT need to reflect the app UI 1:1.
You may crop, frame, abstract, or stylize the app screens to improve clarity and conversion.
2. Editable Figma File
This is very important.
All text in the screenshots must be:
• Easily editable in Figma
• Not baked into images
• Structured so we can localize into multiple languages (EN, NL, DE, FR, ES)
Think:
• Text layers
• Components
• Smart layout for longer translations
⸻
Style & Visual Direction
We like:
• Clean gradients
• Medlo orange / trustworthy colors
• Real people (optional but preferred)
• Subtle medical cues (e.g. bandage / plaster on arm)
We specifically like the first screenshot of this competitor:
👉 https://apps.quorvane.example/us/app/shotlog-tracker/id4827150396
(The woman with a bandage on her arm works very well.)
We want a similar level of polish, but not a copy.
We strongly encourage designers to explore two visual directions:
• A safe, refined direction closely aligned with the current app UI
• A more conceptual / aspirational direction focused on trust, peace of mind, and emotional reassurance
We are open to combining the best elements of both.
Color guidance:
Medlo’s brand color is orange.
Designs should feel medical and trustworthy, but must remain clearly aligned with our brand.
Avoid switching to generic blue-only medical palettes.
⸻
What We Don’t Want
• Overly playful or childish designs
• Overloaded screens
• Technical / developer-style visuals
• Stock images that feel fake or cheesy
⸻
Deliverables
• App Store screenshot designs (iphone and ipad)
• Fully editable Figma file
• Clear text hierarchy
• Ready for localization
⸻
Success Criteria
Primary goal:
Increase App Store page conversion (install rate).
A successful design:
• Looks immediately trustworthy
• Clearly communicates value in <3 seconds
• Feels competitive with top health apps
• Improves App Store conversion
⸻
References
Our app (current version):
https://apps.quorvane.example/us/app/medlo-vaccination-record/id7381029546
Competitor we admire visually:
https://apps.quorvane.example/us/app/shotlog-tracker/id4827150396
⸻
Extra Context (Optional for Designers)
This app already has:
• 200k users
• Active international expansion
• Paid subscriptions
This is not a hobby project — we are investing in quality.

```html
<!DOCTYPE html>
<html lang="en">
<head>
<meta charset="utf-8">
<title>Personalised travel health advice</title>
<link href="https://fonts.googleapis.com/css2?family=Outfit:wght@600;700;800&family=Poppins:wght@400;500;600;700&display=swap" rel="stylesheet">
<style>
  :root{
    --orange:#FFB300;
    --orange-light:#FFC61A;
    --cream:#FFF4DA;
    --ink:#2A2A2A;
    --grey-text:#6E6E6E;
    --card:#F2F3F2;
    --frame:#3A3A3A;
    --frame-dark:#1E1E1E;
    --white:#FFFFFF;
    --line:#E6E6E6;
  }
  *{margin:0;padding:0;box-sizing:border-box}
  html,body{width:1200px;height:2270px;overflow:hidden;background:var(--cream)}
  .canvas{position:relative;width:810px;height:1532px;transform:scale(1.48148);transform-origin:0 0;overflow:hidden;font-family:"Poppins",sans-serif;color:var(--ink)}
  .backdrop{position:absolute;inset:0}
  .abs{position:absolute}
  .eyebrow{left:82px;top:40px;height:44px;padding:0 18px 0 20px;background:var(--white);border-radius:22px;display:flex;align-items:center;gap:8px;font-family:"Outfit",sans-serif;font-weight:600;font-size:19px;letter-spacing:-.3px;white-space:nowrap}
  .headline{left:82px;top:96px;font-family:"Outfit",sans-serif;font-weight:700;font-size:63px;line-height:66px;letter-spacing:-2px;color:var(--ink);white-space:nowrap}
  .phone-frame{left:126px;top:264px;width:560px;height:1238px;border-radius:86px;background:var(--frame);box-shadow:0 0 0 3px var(--frame-dark) inset}
  .phone-btn{background:var(--frame);border-radius:3px}
  .screen{left:140px;top:279px;width:531px;height:1208px;border-radius:72px;background:var(--white);overflow:hidden}
  .screen-fade{position:absolute;left:0;bottom:0;width:100%;height:160px;background:linear-gradient(180deg,rgba(255,255,255,0),#F6F6F6)}
  .tabbar{position:absolute;left:30px;bottom:0;width:473px;height:77px;border-radius:34px 34px 0 0;background:var(--white);box-shadow:0 -2px 14px rgba(0,0,0,.06)}
  .status-time{left:224px;top:305px;font-family:"Outfit",sans-serif;font-weight:600;font-size:22px}
  .island{left:335px;top:298px;width:151px;height:43px;border-radius:22px;background:#000}
  .greeting{left:168px;top:364px;font-weight:600;font-size:30px;letter-spacing:-.6px;white-space:nowrap}
  .bell{left:596px;top:363px;width:47px;height:47px;border-radius:50%;border:1px solid #DADADA;display:flex;align-items:center;justify-content:center}
  .tab{top:431px;height:48px;border-radius:24px;display:flex;align-items:center;justify-content:center;gap:8px;font-weight:600;font-size:11px;letter-spacing:.2px;white-space:nowrap}
  .tab-health{left:174px;width:228px;border:1px solid #D6D6D6;color:var(--ink)}
  .tab-travel{left:411px;width:228px;background:linear-gradient(90deg,var(--orange-light),var(--orange));color:var(--white)}
  .planner-card{left:170px;top:514px;width:473px;height:247px;border-radius:18px;background:var(--card)}
  .planner-icon{left:191px;top:545px;width:58px;height:44px;border-radius:22px;background:linear-gradient(135deg,var(--orange-light),var(--orange))}
  .planner-title{left:269px;top:540px;font-weight:600;font-size:19px;line-height:25px;letter-spacing:-.2px;white-space:nowrap}
  .planner-text{left:269px;top:600px;font-size:13px;line-height:21px;color:var(--grey-text);white-space:nowrap}
  .planner-btn{left:211px;top:669px;width:393px;height:58px;border-radius:29px;background:linear-gradient(90deg,var(--orange-light),var(--orange));color:var(--white);display:flex;align-items:center;justify-content:center;gap:8px;font-weight:600;font-size:14px;white-space:nowrap}
  .section-title{left:170px;top:793px;font-weight:600;font-size:19px}
  .section-text{left:170px;top:825px;font-size:13px;color:var(--grey-text);white-space:nowrap}
  .trip{left:170px;width:473px;height:77px;border-radius:16px;background:var(--card)}
  .trip-flag{position:absolute;left:22px;top:16px;width:46px;height:46px;border-radius:50%;background:var(--white);display:flex;align-items:center;justify-content:center}
  .trip-flag span{width:28px;height:28px;border-radius:50%}
  .flag-lk{background:linear-gradient(90deg,#1E7A3C 0 18%,#F08A1D 18% 34%,#8C1D2A 34%)}
  .flag-ke{background:linear-gradient(180deg,#111 0 33%,#fff 33% 37%,#B4121B 37% 63%,#fff 63% 67%,#1E7A3C 67%)}
  .trip-name{position:absolute;left:84px;top:27px;font-weight:600;font-size:15px}
  .trip-date{position:absolute;right:25px;top:29px;font-size:12.5px;color:var(--grey-text);display:flex;align-items:center;gap:8px;white-space:nowrap}
  .alerts-icon{left:176px;top:1058px;width:48px;height:48px;border-radius:50%;border:1px solid #DADADA;display:flex;align-items:center;justify-content:center}
  .alerts-icon span{width:26px;height:20px;border-radius:10px;background:linear-gradient(135deg,var(--orange-light),var(--orange))}
  .alerts-title{left:236px;top:1062px;font-weight:600;font-size:14px;white-space:nowrap}
  .alerts-text{left:236px;top:1087px;font-size:12px;color:var(--grey-text);white-space:nowrap}
  .toggle{left:597px;top:1070px;width:46px;height:28px;border-radius:14px;background:var(--orange)}
  .toggle::after{content:"";position:absolute;right:3px;top:3px;width:22px;height:22px;border-radius:50%;background:var(--white)}
  .divider{left:170px;top:1135px;width:473px;height:1px;background:var(--line)}
  .footnote{left:170px;top:1162px;font-size:12.5px;color:var(--grey-text);white-space:nowrap}
  .nav-item{top:1428px;width:80px;display:flex;flex-direction:column;align-items:center;gap:6px;font-weight:500;font-size:11px;color:var(--ink);white-space:nowrap}
  .nav-item.active{color:var(--orange)}
  .action-disc{left:295px;top:1420px;width:220px;height:220px;border-radius:50%;background:linear-gradient(135deg,var(--orange-light),var(--orange))}
</style>
</head>
<body>
<div class="canvas">
  <svg class="backdrop" width="810" height="1532" viewBox="0 0 810 1532" aria-hidden="true">
    <defs>
      <linearGradient id="topGlow" x1="0" y1="0" x2="1" y2="1">
        <stop offset="0" stop-color="#FFB000"/>
        <stop offset="1" stop-color="#FFC414"/>
      </linearGradient>
    </defs>
    <rect width="810" height="1532" fill="#FFF4DA"/>
    <path d="M0 0H810V470Q700 600 470 610Q200 620 0 540Z" fill="url(#topGlow)"/>
    <path d="M-20 705Q110 760 210 880" fill="none" stroke="#FFB300" stroke-width="44"/>
    <path d="M670 1010Q740 1130 830 1160" fill="none" stroke="#FFB300" stroke-width="44"/>
  </svg>

  <div class="abs eyebrow">
    <svg width="24" height="16" viewBox="0 0 24 16"><path d="M12 1C6 1 2 8 2 8s4 7 10 7 10-7 10-7-4-7-10-7z" fill="none" stroke="#2A2A2A" stroke-width="2.4"/><circle cx="12" cy="8" r="3" fill="#2A2A2A"/></svg>
    Keep an Overview
  </div>
  <h1 class="abs headline">Personalised travel<br>health advice</h1>

  <div class="abs phone-btn" style="left:120px;top:470px;width:6px;height:40px"></div>
  <div class="abs phone-btn" style="left:120px;top:545px;width:6px;height:80px"></div>
  <div class="abs phone-btn" style="left:120px;top:645px;width:6px;height:80px"></div>
  <div class="abs phone-btn" style="left:685px;top:600px;width:6px;height:120px"></div>
  <div class="abs phone-frame"></div>
  <div class="abs screen">
    <div class="screen-fade"></div>
    <div class="tabbar"></div>
  </div>

  <div class="abs status-time">9:41</div>
  <div class="abs island"></div>
  <svg class="abs" style="left:520px;top:308px" width="108" height="22" viewBox="0 0 108 22" aria-hidden="true">
    <rect x="0" y="13" width="4" height="6" rx="1" fill="#111"/><rect x="6" y="10" width="4" height="9" rx="1" fill="#111"/><rect x="12" y="6" width="4" height="13" rx="1" fill="#111"/><rect x="18" y="3" width="4" height="16" rx="1" fill="#111"/>
    <path d="M36 8a15 15 0 0 1 20 0M40 12a9 9 0 0 1 12 0" fill="none" stroke="#111" stroke-width="2.6" stroke-linecap="round"/><circle cx="46" cy="16" r="2.4" fill="#111"/>
    <rect x="70" y="4" width="32" height="15" rx="4" fill="none" stroke="#111" stroke-width="1.5"/><rect x="72.5" y="6.5" width="27" height="10" rx="2" fill="#111"/><rect x="103" y="9" width="2" height="5" rx="1" fill="#111"/>
  </svg>

  <div class="abs greeting">Hello James</div>
  <div class="abs bell">
    <svg width="22" height="24" viewBox="0 0 22 24"><path d="M11 2a6 6 0 0 0-6 6v5l-2 4h16l-2-4V8a6 6 0 0 0-6-6z" fill="#2A2A2A"/><circle cx="11" cy="20" r="2.5" fill="#2A2A2A"/><circle cx="17" cy="4" r="4" fill="#E53935" stroke="#fff" stroke-width="1.5"/></svg>
  </div>

  <div class="abs tab tab-health">
    <svg width="20" height="18" viewBox="0 0 20 18"><path d="M10 17S1 11 1 5.5A4.5 4.5 0 0 1 10 3a4.5 4.5 0 0 1 9 2.5C19 11 10 17 10 17z" fill="#FFB300"/><path d="M3 9h4l1.5-3 2.5 6 1.5-3H17" fill="none" stroke="#fff" stroke-width="1.5"/></svg>
    PERSONAL HEALTH
  </div>
  <div class="abs tab tab-travel">
    <svg width="18" height="18" viewBox="0 0 24 24"><path d="M21 16v-2l-8-5V3.5a1.5 1.5 0 0 0-3 0V9l-8 5v2l8-2.5V19l-2 1.5V22l3.5-1 3.5 1v-1.5L13 19v-5.5z" fill="#fff" transform="rotate(45 12 12)"/></svg>
    TRAVEL
  </div>

  <div class="abs planner-card"></div>
  <div class="abs planner-icon" role="img" aria-label="Globe with aeroplane icon"></div>
  <div class="abs planner-title">Discover which vaccinations you<br>need for your next trip</div>
  <div class="abs planner-text">See which vaccinations you need and<br>where to get them.</div>
  <div class="abs planner-btn">
    <svg width="18" height="18" viewBox="0 0 24 24"><path d="M21 16v-2l-8-5V3.5a1.5 1.5 0 0 0-3 0V9l-8 5v2l8-2.5V19l-2 1.5V22l3.5-1 3.5 1v-1.5L13 19v-5.5z" fill="#fff" transform="rotate(45 12 12)"/></svg>
    START TRAVEL PLANNER
  </div>

  <div class="abs section-title">My Trips</div>
  <div class="abs section-text">Stay updated on your travel vaccinations.</div>

  <div class="abs trip" style="top:860px">
    <div class="trip-flag"><span class="flag-lk" role="img" aria-label="Sri Lanka flag"></span></div>
    <div class="trip-name">Sri Lanka</div>
    <div class="trip-date">
      <svg width="14" height="14" viewBox="0 0 14 14"><rect x="1" y="2" width="12" height="11" rx="2" fill="none" stroke="#FFB300" stroke-width="1.3"/><path d="M1 5.5h12M4 1v2.5M10 1v2.5" stroke="#FFB300" stroke-width="1.3"/></svg>
      Departing. Jan 14, 2028
    </div>
  </div>
  <div class="abs trip" style="top:946px">
    <div class="trip-flag"><span class="flag-ke" role="img" aria-label="Kenya flag"></span></div>
    <div class="trip-name">Kenia</div>
    <div class="trip-date">
      <svg width="14" height="14" viewBox="0 0 14 14"><rect x="1" y="2" width="12" height="11" rx="2" fill="none" stroke="#FFB300" stroke-width="1.3"/><path d="M1 5.5h12M4 1v2.5M10 1v2.5" stroke="#FFB300" stroke-width="1.3"/></svg>
      Departing. Jan 17, 2028
    </div>
  </div>

  <div class="abs alerts-icon"><span role="img" aria-label="Globe with aeroplane icon"></span></div>
  <div class="abs alerts-title">Travel notification reminders</div>
  <div class="abs alerts-text">You’ll get notified about relevant travel alerts.</div>
  <div class="abs toggle"></div>
  <div class="abs divider"></div>
  <div class="abs footnote">You know when discover or vaccination advice for your destinations</div>

  <div class="abs nav-item active" style="left:182px">
    <svg width="24" height="22" viewBox="0 0 24 22"><path d="M12 1 1 10h3v11h6v-6h4v6h6V10h3z" fill="#FFB300"/></svg>
    Home
  </div>
  <div class="abs nav-item" style="left:280px">
    <svg width="26" height="24" viewBox="0 0 26 24"><path d="M4 22l4-4m0 0 10-10 3 3-10 10zm10-10 2 2m-5 1 2 2M18 8l3-3m-1-2 4 4" fill="none" stroke="#2A2A2A" stroke-width="1.8" stroke-linecap="round"/></svg>
    Vaccinations
  </div>
  <div class="abs nav-item" style="left:466px">
    <svg width="24" height="22" viewBox="0 0 24 22"><rect x="2" y="4" width="18" height="16" rx="2" fill="none" stroke="#2A2A2A" stroke-width="1.8"/><path d="M4 18l5-6 4 4 3-3 4 5" fill="#2A2A2A"/><path d="M20 0v6M17 3h6" stroke="#2A2A2A" stroke-width="1.8"/></svg>
    Uploads
  </div>
  <div class="abs nav-item" style="left:545px">
    <svg width="24" height="24" viewBox="0 0 24 24"><path d="M10 1h4l.6 3 2.3 1 2.6-1.7 2.8 2.8L20.6 9l1 2.3 3 .7v4l-3 .6-1 2.3 1.7 2.6-2.8 2.8-2.6-1.7-2.3 1-.6 3h-4l-.6-3-2.3-1-2.6 1.7-2.8-2.8L3.4 19l-1-2.3-3-.7v-4l3-.6 1-2.3-1.7-2.6 2.8-2.8L7.1 5l2.3-1z" transform="scale(.92) translate(1 1)" fill="#2A2A2A"/><circle cx="12" cy="12" r="3.6" fill="#fff"/></svg>
    Settings
  </div>
  <div class="abs action-disc" role="img" aria-label="Travel planner button with globe and aeroplane icon"></div>
</div>
</body>
</html>
```